Etiketten für Brennerei
Wir haben viele kreative Vorschläge für unser neues Etikett erhalten und uns schlussendlich für dieses Design von m2741 entschieden. Bei allen Berwerben und vor allem bei m2741 hat uns gefallen, dass Anmerkungen und Wünsche zum Abändern des Designs direkt umgesetzt wurden. Die Wartezeiten waren sehr kurz und wir können das Portal und diesen Designer nur wärmstens empfehlen.
Zielgruppe
Wir haben eine kleine familiengeführte Brennerei in Karlsruhe (Baden-Württemberg). Wir bieten unseren Kunden vor allem Gin, Whisky und Edeldestillate an. Wir gehen davon aus, dass die Zielgruppe unseres Moosfink Gins eher kreative, lustige und unkonventionelle Dinge bevorzugt.
Aufgabenstellung
Das Flaschenetikett ist für die Vorderseite eines schwarz gefärbten Gins mit dem Namen Moosfink. Der Moosfink sollte in irgendeiner Weise im Design vorkommen. Ansonsten ist es nur wichtig, dass das Design auffällig ist. Es können passende Stockillustrationen oder eigene Illustrationen verwendet werden. Die Flaschenform ist als Bilddatei hinterlegt.

```html
<!DOCTYPE html>
<html lang="de">
<head>
<meta charset="utf-8">
<title>Moosfink Gin – Etikett</title>
<link rel="stylesheet" href="https://fonts.googleapis.com/css2?family=Bebas+Neue&family=Fredoka:wght@600&display=swap">
<style>
  :root {
    --canvas-bg: #d9d9d9;
    --label-paper: #ebebea;
    --ink: #1c1c1b;
    --gold: #d8a532;
    --bird-grey: #8a8886;
    --bird-light: #cfcac6;
  }
  * { box-sizing: border-box; margin: 0; padding: 0; }
  html, body {
    width: 900px;
    height: 1200px;
    overflow: hidden;
    background: var(--canvas-bg);
  }
  .artboard {
    position: relative;
    width: 900px;
    height: 1200px;
  }

  /* Neck strip */
  .neck-strip {
    position: absolute;
    left: 70px;
    top: 300px;
    width: 74px;
    height: 420px;
    background: var(--label-paper);
    display: flex;
    flex-direction: column;
    align-items: center;
    padding-top: 18px;
  }
  .neck-strip__name {
    writing-mode: vertical-rl;
    font-family: "Bebas Neue", "Oswald", sans-serif;
    font-size: 54px;
    letter-spacing: 1px;
    color: var(--ink);
    line-height: 1;
  }
  .neck-strip__bird {
    margin-top: auto;
    margin-bottom: 40px;
    width: 58px;
    height: 44px;
    border-radius: 50% 45% 40% 50%;
    background: radial-gradient(circle at 40% 40%, var(--bird-light), var(--bird-grey));
  }

  /* Front label */
  .front-label {
    position: absolute;
    left: 180px;
    top: 280px;
    width: 640px;
    height: 640px;
    border-radius: 50%;
    overflow: hidden;
    background: var(--label-paper);
  }
  .front-label__bird {
    position: absolute;
    left: 185px;
    top: 98px;
    width: 300px;
    height: 170px;
    border-radius: 50% 45% 40% 55%;
    background: radial-gradient(ellipse at 35% 40%, var(--bird-light), var(--bird-grey) 70%);
  }
  .front-label__name {
    position: absolute;
    left: 0;
    right: 0;
    top: 262px;
    text-align: center;
    font-family: "Bebas Neue", "Oswald", sans-serif;
    font-size: 128px;
    line-height: 104px;
    letter-spacing: 4px;
    color: var(--ink);
  }
  .front-label__band {
    position: absolute;
    left: 0;
    right: 0;
    bottom: 0;
    height: 168px;
    background: var(--ink);
    display: flex;
    justify-content: center;
    align-items: flex-start;
  }
  .front-label__kind {
    font-family: "Fredoka", "Varela Round", sans-serif;
    font-weight: 600;
    font-size: 150px;
    line-height: 1;
    margin-top: 8px;
    letter-spacing: 4px;
    color: var(--gold);
  }
</style>
</head>
<body>
  <main class="artboard">
    <aside class="neck-strip">
      <span class="neck-strip__name">MOOSFINK</span>
      <div class="neck-strip__bird" role="img" aria-label="Kleine Illustration eines Vogels"></div>
    </aside>

    <section class="front-label">
      <div class="front-label__bird" role="img" aria-label="Gezeichneter, zerzauster Spatz in Grau und Schwarz"></div>
      <h1 class="front-label__name">MOOS<br>FINK</h1>
      <div class="front-label__band">
        <span class="front-label__kind">GIN</span>
      </div>
    </section>
  </main>
</body>
</html>
```